Amber Burrows Business Card Design

Amber Burrows - Gathering Gentle Meadow Corners

Amber Burrows is a company that focuses on promoting the design, construction, consultation and support of natural, creative and organic play spaces for Early Childhood and learning environments.

We need a professional Business Card designed that is unique modern and creative. The Philosophy of the company is nostalgic so the business and will need to reflect this but also reflect that our ideas are modern and cutting edge.

The business card will need to be a talking point, by either having a unique size, quality and/or placement of logo or other quality.

I am more interested in using natural recycled paper, as this would reflect the philosophy of the company, but I open to seeing colour used creatively.
Updates

Hi Designers, Apologies, Could you please add www.amberburrows.com.au to the business card. Thanks very much.

Hi All, Thank you all for your submission thus far. Please note the fonts for used in the logo are: Ostrich Sans Black and Archer Semi Bold. If these could be considered for contact details, my name etc. Also please show the design on a recycled brown card if possible as this will be the type of card I will use when printing. Thanks so much.

Target Market(s)

Child Care Providers, Play Industry Professionals

Industry/Entity Type

Business

Contact Information for Business Card

Amber Burrows
Gathering Gentle Meadow Corners
Marguerite Holloway
0419 862 503
marguerite@amberburrows.com.au

Font styles to use
Sans Serif

Requirements
Must have
• The Logo and the Details plus the below phrase
• Amber Burrows - Gathering Gentle Meadow Corners
Nice to have
• A bit of colour, but not too much colour.
Should not have
• Not to have a white background, recycled brown card only

```html
<!DOCTYPE html>
<html lang="en">
<head>
<meta charset="utf-8">
<title>Amber Burrows Business Card Design</title>
<link href="https://fonts.googleapis.com/css2?family=Arvo:wght@400;700&display=swap" rel="stylesheet">
<style>
  :root {
    --backdrop: #5b4637;
    --card-front: #262626;
    --card-back: #b39c80;
    --ink-light: #f4f1ec;
    --ink-dark: #1d1a17;
  }
  html, body {
    margin: 0;
    padding: 0;
    width: 1200px;
    height: 1000px;
    overflow: hidden;
    background: var(--backdrop);
  }
  .canvas {
    position: relative;
    width: 1200px;
    height: 1000px;
  }
  .card {
    position: absolute;
    left: 236px;
    width: 727px;
    height: 415px;
    box-shadow: 0 6px 18px rgba(0,0,0,0.35);
  }
  .card--front {
    top: 72px;
    background: var(--card-front);
    color: var(--ink-light);
  }
  .card--back {
    top: 513px;
    background: var(--card-back);
    color: var(--ink-dark);
  }
  .brand-mark {
    position: absolute;
    left: 313px;
    top: 88px;
    width: 100px;
    height: 100px;
    border-radius: 50%;
    border: 2px solid var(--ink-light);
    box-sizing: border-box;
  }
  .brand-est {
    position: absolute;
    top: 197px;
    left: 0;
    width: 100%;
    display: flex;
    justify-content: center;
    gap: 64px;
    font-family: "Arvo", serif;
    font-size: 19px;
    letter-spacing: 1px;
  }
  .brand-name {
    position: absolute;
    top: 226px;
    left: 0;
    width: 100%;
    text-align: center;
    margin: 0;
    font-family: "Arvo", serif;
    font-weight: 700;
    font-size: 46px;
    letter-spacing: 2px;
    text-transform: uppercase;
    line-height: 1;
  }
  .brand-tagline {
    position: absolute;
    top: 288px;
    left: 0;
    width: 100%;
    text-align: center;
    margin: 0;
    font-family: "Arvo", serif;
    font-size: 15px;
    line-height: 21px;
    letter-spacing: 1px;
    text-transform: uppercase;
  }
  .brand-flourish {
    position: absolute;
    left: 318px;
    top: 334px;
    width: 90px;
    height: 14px;
    background: rgba(244,241,236,0.55);
  }
  .contact {
    position: absolute;
    left: 180px;
    width: 370px;
    top: 138px;
    text-align: center;
    font-family: "Arvo", serif;
  }
  .contact__name {
    margin: 0;
    font-size: 19px;
    font-weight: 400;
    letter-spacing: 1.5px;
    text-transform: uppercase;
  }
  .contact__rule {
    width: 60px;
    height: 1.5px;
    background: var(--ink-dark);
    margin: 12px auto 22px;
  }
  .contact__line {
    margin: 0;
    font-size: 16.5px;
    line-height: 28px;
    letter-spacing: 0.3px;
  }
</style>
</head>
<body>
  <main class="canvas">
    <section class="card card--front" aria-label="Business card front">
      <div class="brand-mark" aria-hidden="true"></div>
      <div class="brand-est"><span>EST</span><span>2015</span></div>
      <h1 class="brand-name">Amber Burrows</h1>
      <p class="brand-tagline">Gathering<br>Gentle Meadow Corners</p>
      <div class="brand-flourish" role="img" aria-label="Small decorative flourish under the tagline"></div>
    </section>

    <section class="card card--back" aria-label="Business card back">
      <div class="contact">
        <h2 class="contact__name">Marguerite Holloway</h2>
        <div class="contact__rule"></div>
        <p class="contact__line">0419 862 503</p>
        <p class="contact__line">marguerite@amberburrows.com.au</p>
        <p class="contact__line">www.amberburrows.com.au</p>
      </div>
    </section>
  </main>
</body>
</html>
```